Property Developer - Simple yet Sophisticated and Sharp Business Card

We are a medium sized property developer involved mainly in townhouse developments and land subdivisions.

The company is looking for a simple, sharp and sophisticated business card that will be given to contractors, land owners, financiers etc and thus will need to look professional.

Property development related graphics and art can be used, however the card is not to be too "busy" or crowded. Our company name is KL Estates which could possibly be incorporated into the graphics or artwork.

Single sided and/or double sided designs will be acceptable.

A Simple, Sophisticated, Sharp design please!

Good Luck !

```html
<!DOCTYPE html>
<html lang="en">
<head>
<meta charset="utf-8">
<title>KL Estates – Business Card</title>
<link rel="stylesheet" href="https://fonts.googleapis.com/css2?family=Share+Tech+Mono&display=swap">
<style>
  :root {
    --page: #ffffff;
    --card: #ffffff;
    --card-edge: #8a8a8a;
    --band: #b3201b;
    --ink-light: #f4e6e4;
  }
  html, body {
    margin: 0;
    width: 1200px;
    height: 900px;
    overflow: hidden;
    background: var(--page);
  }
  .business-card {
    position: absolute;
    left: 66px;
    top: 126px;
    width: 1066px;
    height: 648px;
    box-sizing: border-box;
    border: 1px solid var(--card-edge);
    background: var(--card);
  }
  .brand-band {
    position: absolute;
    left: 0;
    right: 0;
    top: 206px;
    height: 236px;
    background: var(--band);
  }
  .contact-text {
    position: absolute;
    margin: 0;
    font-family: "Share Tech Mono", monospace;
    font-size: 21px;
    line-height: 30px;
    letter-spacing: 4.6px;
    text-transform: uppercase;
    color: var(--ink-light);
  }
  .person {
    top: 42px;
    right: 618px;
    text-align: right;
  }
  .divider {
    position: absolute;
    left: 447px;
    top: 34px;
    width: 2px;
    height: 170px;
    background: var(--ink-light);
  }
  .company-details {
    top: 42px;
    left: 469px;
    text-align: left;
  }
  .contact-text span { display: block; }
</style>
</head>
<body>
  <div class="business-card">
    <div class="brand-band">
      <p class="contact-text person">
        <span class="person-name">Mark Ellison</span>
        <span class="person-role">Project Manager</span>
      </p>
      <div class="divider"></div>
      <p class="contact-text company-details">
        <span class="company-name">KL Estates</span>
        <span class="phone">P (07) 3054 8816</span>
        <span class="fax">F (07) 3054 8817</span>
        <span class="email">E projects.klestates@mailbox.com</span>
        <span class="address">PO Box 2875 Riverton North QLD 4102</span>
      </p>
    </div>
  </div>
</body>
</html>
```